Velvet Arc Car Detailing Brochure

I would like a trifold brochure designed for my car detailing business. The background has to be full black or mostly black with some designing using only colors present in our logo.

Front page must have our logo and name, list of services, a photo and mybe our phone number but no long text.

Inside I want to present each service one by one with its description and a photo representing/showing each service. (I will provide the text below). For photos, use stock photos and I will add come of mines already too.

On the back of the brochure I want to have contact & info: phone number, opening hours, address, website, Instagram.

Outside left I want the text About us and photo/design.

I want the brochure to be neat, professional, easy to read, but at the same time not too boring.

Text:
1. About us
a. the ultimate destination for car care in Geneva. We provide personalized, detail-oriented services that bring out the best in your car. With our expert techniques and dedicated approach, we ensure that your car receives the utmost care and attention. Experience a place where passion meets precision and let us create an exceptional car care experience designed just for you.
2. Services:

DETAILING & HAND WASH

• Comprehensive exterior & interior care
• Personalisation and tailored cleaning packages
• Decontamination
• Premium products
• Attention to detail for a perfect finish

POLISHING

• Eliminates scratches, holograms
• Revives and protects paint
• Ensures lasting gloss
• Enhances paint life
• Preserves car’s value and beauty

CERAMIC TREATMENT

• Durable paint protection
• Water-repellent (hydrophobic) effect
• Easier cleaning, enhanced shine
• Long-term surface safeguarding
• Shields against environmental impacts

DRY ICE WASH

• Innovative, waterless method
• Safe for all car parts
• Deep cleans, removes odors
• Allergen-free, antibacterial
• Gentle, effective
• Advanced cleaning technology

COVERING

• Personalized vehicle styling
• More than 150 colours available
• Clean cut without using a cutter
• High-quality, durable materials
• Custom designs available

PROTECTION FILM

• Invisible, durable shield
• Self-healing technology
• 10-year warranty by RQ FOLV

DETAILING BOUTIQUE

• Premium brands available
• Buy on site during your visit
• Granite Assembly, Pip Autos, DRAV Norra
• Essential for at-home car care
• Perfect for quick touch-ups
(for these three brands you can put their logos

Target Market(s)

Our target market includes car owners of all price ranges, with a special focus on those who are passionate about their vehicles. We cater to clients who value excellent service and results, and seek to maintain their cars in pristine condition.

Industry/Entity Type

Automobile / Car detailing

Colors

Designer to choose colors to be used in the design.

Requirements
Must have
• Brand Consistency: The brochure must adhere to our brand colors and style, particularly utilizing the colors present in our logo. Trifold Layout: The design must be specifically tailored for a trifold brochure format. Legibility: Text must be easy to read against the mostly black background, with appropriate font size and style. Professional Look and Feel: The overall design must convey professionalism while being engaging and not overly complex. Photo representation: each service description should have a phot presenting it.
Should not have
• Overcrowded Design: Avoid cluttering with too much text or too many images. The layout should be clean and easy to navigate. Cartoonish Fonts or Graphics: Avoid using unprofessional or casual fonts and graphics that do not align with the upscale and professional image of our business. Distracting Backgrounds: The background should complement and not overpower the content. Stick to the theme of mostly black with design elements from our logo.

```html
<!DOCTYPE html>
<html lang="en">
<head>
<meta charset="utf-8">
<title>Velvet Arc Car Detailing – Trifold Brochure</title>
<link rel="stylesheet" href="https://fonts.googleapis.com/css2?family=Montserrat:wght@400;500;600&family=Saira+Condensed:ital,wght@0,600;0,700;1,800&display=swap">
<style>
  :root{
    --ink:#08080b;
    --panel:#0e0e13;
    --pink:#d93695;
    --blue:#2b93dc;
    --deep-blue:#0f4f86;
    --text:#f1f1f4;
    --muted:#b9bac4;
    --stage:#e6e4e1;
  }
  *{box-sizing:border-box;margin:0;padding:0}
  html,body{width:1200px;height:675px;overflow:hidden}
  body{background:var(--stage);font-family:"Montserrat",sans-serif;color:var(--text);position:relative}
  .defs{position:absolute;width:0;height:0}
  .sheet{position:absolute;top:118px;width:565px;height:440px;display:flex;box-shadow:0 10px 30px rgba(0,0,0,.28)}
  .sheet--inside{left:25px}
  .sheet--outside{left:610px}
  .panel{position:relative;width:33.333%;height:100%;background:var(--panel);padding:18px 12px 14px;overflow:hidden}
  .panel + .panel{border-left:1px solid #1d1d25}
  .panel--glow{background:radial-gradient(120% 60% at 80% 30%,#1a2a45 0%,var(--panel) 60%)}
  .panel--violet{background:linear-gradient(180deg,var(--panel) 55%,#24142a 100%)}

  .hex{display:block;flex:0 0 auto}
  .service{position:relative;margin-bottom:18px}
  .service__head{display:flex;align-items:center;gap:6px;margin-bottom:5px}
  .service__head--right{flex-direction:row-reverse;justify-content:space-between}
  .service__title{font-family:"Saira Condensed",sans-serif;font-weight:700;font-size:14.5px;line-height:1;white-space:nowrap;background:linear-gradient(90deg,var(--pink),var(--blue));-webkit-background-clip:text;background-clip:text;color:transparent}
  .bullets{list-style:none;font-size:7px;line-height:1.45;color:var(--text)}
  .bullets li{padding-left:8px;position:relative}
  .bullets li::before{content:"";position:absolute;left:1px;top:4px;width:3px;height:3px;background:var(--text)}

  .web{position:absolute;left:0;right:0;bottom:14px;display:flex;justify-content:center;align-items:center;gap:5px;font-size:9px;color:var(--text)}
  .dot-icon{width:9px;height:9px;border-radius:50%;background:linear-gradient(135deg,var(--pink),var(--blue))}

  .brand-grid{display:grid;grid-template-columns:1fr 1fr;gap:5px;margin:12px 0 14px}
  .brand-tile{height:22px;background:#16161d;border:1px solid #24242e}
  .brand-tile--wide{grid-column:1 / 3}
  .feature-photo{display:block;margin:0 auto}
  .phone-line{display:flex;justify-content:center;align-items:center;gap:6px;font-size:11px;font-weight:500;margin-top:10px}

  .about__title{font-family:"Saira Condensed",sans-serif;font-weight:700;font-size:20px;color:var(--pink);margin:14px 0 6px}
  .about__text{font-size:7px;line-height:1.55;color:var(--muted);margin-bottom:8px}

  .contact__title{font-family:"Saira Condensed",sans-serif;font-weight:700;font-size:20px;color:var(--pink);margin:10px 0 10px}
  .contact__item{display:flex;gap:6px;margin-bottom:9px}
  .contact__label{font-size:9px;font-weight:600}
  .contact__value{font-size:8.5px;color:var(--text);line-height:1.35}
  .icon{flex:0 0 10px;margin-top:1px}

  .cover{background:linear-gradient(180deg,var(--panel) 0%,var(--ink) 45%,var(--deep-blue) 70%,#0b2340 100%);text-align:left}
  .brand{display:flex;align-items:center;justify-content:center;gap:6px;margin-top:4px}
  .brand__mark{width:18px;height:18px;border-radius:50%;border:1.5px solid var(--pink)}
  .brand__name{font-size:8px;font-weight:500;letter-spacing:.5px;color:var(--text)}
  .cover__title{font-family:"Saira Condensed",sans-serif;font-style:italic;font-weight:800;font-size:34px;line-height:.92;text-align:center;margin-top:18px}
  .cover__title .line-blue{color:var(--blue);display:block}
  .cover__title .line-pink{color:var(--pink);display:block}
  .cover__photo{display:block;margin:12px auto 0;width:160px;height:78px;border-radius:6px;background:radial-gradient(60% 55% at 50% 55%,#e9ecf0 0%,#9aa1ab 55%,transparent 100%)}
  .cover__tagline{font-family:"Saira Condensed",sans-serif;font-weight:600;font-size:14px;line-height:1.1;margin:14px 0 8px}
  .cover__list{font-size:8.5px;line-height:1.5}
  .cover__list li::before{top:5px}
  .cover .phone-line{margin-top:12px}
</style>
</head>
<body>

<svg class="defs" aria-hidden="true">
  <defs>
    <linearGradient id="frame" x1="0" y1="0" x2="1" y2="1">
      <stop offset="0" stop-color="#d93695"/><stop offset="1" stop-color="#2b93dc"/>
    </linearGradient>
    <linearGradient id="photo" x1="0" y1="0" x2="1" y2="1">
      <stop offset="0" stop-color="#5b6270"/><stop offset=".55" stop-color="#2a2e37"/><stop offset="1" stop-color="#14161c"/>
    </linearGradient>
    <linearGradient id="photo-light" x1="0" y1="0" x2="1" y2="1">
      <stop offset="0" stop-color="#c9ced6"/><stop offset="1" stop-color="#3b4250"/>
    </linearGradient>
  </defs>
</svg>

<!-- Inside spread -->
<section class="sheet sheet--inside">
  <article class="panel">
    <div class="service">
      <div class="service__head">
        <svg class="hex" width="42" height="39" viewBox="0 0 54 50" role="img" aria-label="Photo of a hand washing a car wheel with foam"><polygon points="14,2 40,2 52,25 40,48 14,48 2,25" fill="url(#photo-light)" stroke="url(#frame)" stroke-width="2"/></svg>
        <h2 class="service__title">Detailing &amp; Hand Wash</h2>
      </div>
      <ul class="bullets">
        <li>Comprehensive exterior &amp; interior care</li>
        <li>Personalisation and tailored cleaning packages</li>
        <li>Decontamination</li>
        <li>Premium products</li>
        <li>Attention to detail for a perfect finish</li>
      </ul>
    </div>
    <div class="service">
      <div class="service__head service__head--right">
        <svg class="hex" width="42" height="39" viewBox="0 0 54 50" role="img" aria-label="Photo of a polishing machine on a car panel"><polygon points="14,2 40,2 52,25 40,48 14,48 2,25" fill="url(#photo)" stroke="url(#frame)" stroke-width="2"/></svg>
        <h2 class="service__title">Polishing</h2>
      </div>
      <ul class="bullets">
        <li>Eliminates scratches, holograms</li>
        <li>Revives and protects paint</li>
        <li>Ensures lasting gloss</li>
        <li>Enhances paint life</li>
        <li>Preserves car’s value and beauty</li>
      </ul>
    </div>
    <div class="service">
      <div class="service__head">
        <svg class="hex" width="42" height="39" viewBox="0 0 54 50" role="img" aria-label="Photo of a ceramic coating applicator on paint"><polygon points="14,2 40,2 52,25 40,48 14,48 2,25" fill="url(#photo-light)" stroke="url(#frame)" stroke-width="2"/></svg>
        <h2 class="service__title">Ceramic Treatment</h2>
      </div>
      <ul class="bullets">
        <li>Durable paint protection</li>
        <li>Water-repellent (hydrophobic) effect</li>
        <li>Easier cleaning, enhanced shine</li>
        <li>Long-term surface safeguarding</li>
        <li>Shields against environmental impacts</li>
      </ul>
    </div>
    <p class="web"><span class="dot-icon"></span>www.velvetarcdetail.com</p>
  </article>

  <article class="panel panel--violet">
    <div class="service">
      <div class="service__head">
        <svg class="hex" width="42" height="39" viewBox="0 0 54 50" role="img" aria-label="Photo of dry ice cleaning of an engine bay"><polygon points="14,2 40,2 52,25 40,48 14,48 2,25" fill="url(#photo-light)" stroke="url(#frame)" stroke-width="2"/></svg>
        <h2 class="service__title">Dry Ice Wash</h2>
      </div>
      <ul class="bullets">
        <li>Innovative, waterless method</li>
        <li>Safe for all car parts</li>
        <li>Deep cleans, removes odors</li>
        <li>Allergen-free, antibacterial</li>
        <li>Gentle, effective</li>
        <li>Advanced cleaning technology</li>
      </ul>
    </div>
    <div class="service">
      <div class="service__head service__head--right">
        <svg class="hex" width="42" height="39" viewBox="0 0 54 50" role="img" aria-label="Photo of a car being wrapped in orange vinyl"><polygon points="14,2 40,2 52,25 40,48 14,48 2,25" fill="url(#photo)" stroke="url(#frame)" stroke-width="2"/></svg>
        <h2 class="service__title">Covering</h2>
      </div>
      <ul class="bullets">
        <li>Personalized vehicle styling</li>
        <li>More than 150 colours available</li>
        <li>Clean cut without using a cutter</li>
        <li>High-quality, durable materials</li>
        <li>Custom designs available</li>
      </ul>
    </div>
    <div class="service">
      <div class="service__head">
        <svg class="hex" width="42" height="39" viewBox="0 0 54 50" role="img" aria-label="Photo of protection film being applied to a headlight"><polygon points="14,2 40,2 52,25 40,48 14,48 2,25" fill="url(#photo)" stroke="url(#frame)" stroke-width="2"/></svg>
        <h2 class="service__title">Protection Film</h2>
      </div>
      <ul class="bullets">
        <li>Invisible, durable shield</li>
        <li>Self-healing technology</li>
        <li>10-year warranty by RQ FOLV</li>
      </ul>
    </div>
    <p class="web"><span class="dot-icon"></span>www.velvetarcdetail.com</p>
  </article>

  <article class="panel">
    <div class="service">
      <div class="service__head">
        <svg class="hex" width="42" height="39" viewBox="0 0 54 50" role="img" aria-label="Photo of a detailer cleaning a steering wheel"><polygon points="14,2 40,2 52,25 40,48 14,48 2,25" fill="url(#photo-light)" stroke="url(#frame)" stroke-width="2"/></svg>
        <h2 class="service__title">Detailing Boutique</h2>
      </div>
      <ul class="bullets">
        <li>Premium brands available</li>
        <li>Buy on site during your visit</li>
        <li>Granite Assembly, Pip Autos, DRAV Norra</li>
        <li>Essential for at-home car care</li>
        <li>Perfect for quick touch-ups</li>
      </ul>
    </div>
    <div class="brand-grid" aria-label="Partner brands">
      <div class="brand-tile"></div>
      <div class="brand-tile"></div>
      <div class="brand-tile brand-tile--wide"></div>
    </div>
    <svg class="feature-photo" width="150" height="140" viewBox="0 0 150 140" role="img" aria-label="Photo of a detailer polishing a white hatchback in a studio"><polygon points="38,3 112,3 147,45 147,110 112,137 38,137 3,110 3,45" fill="url(#photo)" stroke="url(#frame)" stroke-width="3"/></svg>
    <p class="phone-line">
      <svg class="icon" width="11" height="11" viewBox="0 0 12 12" aria-hidden="true"><circle cx="6" cy="6" r="6" fill="var(--pink)"/><path d="M4 3.2l1 1.6-.6.6c.4.8 1 1.4 1.8 1.8l.6-.6 1.6 1-.5 1.2C5.6 8.7 3.3 6.4 3 4z" fill="#fff"/></svg>
      0198 765 4321
    </p>
  </article>
</section>

<!-- Outside spread -->
<section class="sheet sheet--outside">
  <article class="panel panel--glow about">
    <svg class="feature-photo" width="130" height="125" viewBox="0 0 130 125" role="img" aria-label="Photo of a blue polishing machine working on a car interior"><polygon points="32,3 98,3 127,38 127,92 98,122 32,122 3,92 3,38" fill="url(#photo-light)" stroke="url(#frame)" stroke-width="3"/></svg>
    <h2 class="about__title">About Us</h2>
    <p class="about__text">The ultimate destination for car care in Geneva. We provide personalized, detail-oriented services that bring out the best in your car. With our expert techniques and dedicated approach, we ensure that your car receives the utmost care and attention.</p>
    <p class="about__text">Experience a place where passion meets precision and let us create an exceptional car care experience designed just for you.</p>
    <p class="web"><span class="dot-icon"></span>www.velvetarcdetail.com</p>
  </article>

  <article class="panel panel--violet contact">
    <h2 class="contact__title">Get In Touch</h2>
    <div class="contact__item">
      <svg class="icon" width="10" height="10" viewBox="0 0 12 12" aria-hidden="true"><circle cx="6" cy="6" r="6" fill="var(--pink)"/><path d="M4 3.2l1 1.6-.6.6c.4.8 1 1.4 1.8 1.8l.6-.6 1.6 1-.5 1.2C5.6 8.7 3.3 6.4 3 4z" fill="#fff"/></svg>
      <div><p class="contact__label">Phone</p><p class="contact__value">+00 987 654 321</p></div>
    </div>
    <div class="contact__item">
      <svg class="icon" width="10" height="10" viewBox="0 0 12 12" aria-hidden="true"><circle cx="6" cy="6" r="5" fill="none" stroke="var(--pink)" stroke-width="1.6"/><path d="M6 3v3l2 1.3" stroke="var(--pink)" stroke-width="1.3" fill="none"/></svg>
      <div><p class="contact__label">Business Hours</p><p class="contact__value">Mon - Fri : 10 am - 8pm<br>Sat - Sun : Closed</p></div>
    </div>
    <div class="contact__item">
      <svg class="icon" width="10" height="12" viewBox="0 0 10 12" aria-hidden="true"><path d="M5 0a4 4 0 0 1 4 4c0 3-4 8-4 8S1 7 1 4a4 4 0 0 1 4-4z" fill="var(--pink)"/><circle cx="5" cy="4" r="1.5" fill="#fff"/></svg>
      <div><p class="contact__label">Address</p><p class="contact__value">4410 Marlow Street,<br>Fenwick, CA 90210</p></div>
    </div>
    <div class="contact__item">
      <svg class="icon" width="10" height="10" viewBox="0 0 12 12" aria-hidden="true"><circle cx="6" cy="6" r="5" fill="none" stroke="var(--pink)" stroke-width="1.4"/><path d="M1 6h10M6 1c-2.5 3-2.5 7 0 10M6 1c2.5 3 2.5 7 0 10" stroke="var(--pink)" stroke-width="1" fill="none"/></svg>
      <div><p class="contact__label">Web</p><p class="contact__value">www.velvetarcdetail.com</p></div>
    </div>
    <div class="contact__item">
      <svg class="icon" width="10" height="10" viewBox="0 0 12 12" aria-hidden="true"><rect x="1" y="1" width="10" height="10" rx="2" fill="none" stroke="var(--pink)" stroke-width="1.4"/></svg>
      <div><p class="contact__label">Instagram ID</p><p class="contact__value">velvet_arc</p></div>
    </div>
    <svg class="feature-photo" width="110" height="105" viewBox="0 0 110 105" role="img" aria-label="Photo of a hand holding a foam applicator on a car wheel"><polygon points="27,3 83,3 107,32 107,75 83,102 27,102 3,75 3,32" fill="url(#photo-light)" stroke="url(#frame)" stroke-width="3"/></svg>
    <p class="web"><span class="dot-icon"></span>www.velvetarcdetail.com</p>
  </article>

  <article class="panel cover">
    <div class="brand">
      <span class="brand__mark"></span>
      <span class="brand__name">VELVET ARC</span>
    </div>
    <h1 class="cover__title"><span class="line-blue">BEST CAR</span><span class="line-pink">DETAILING</span></h1>
    <div class="cover__photo" role="img" aria-label="Photo of a white hatchback car, three-quarter front view"></div>
    <p class="cover__tagline">Come to the Velvet Arc<br>for auto detailing services</p>
    <ul class="bullets cover__list">
      <li>Detailing &amp; Hand Wash</li>
      <li>Polishing</li>
      <li>Ceramic Treatment</li>
      <li>Dry Ice Wash</li>
      <li>Covering</li>
      <li>Protection Film</li>
      <li>Detailing Boutique</li>
    </ul>
    <p class="phone-line">
      <svg class="icon" width="11" height="11" viewBox="0 0 12 12" aria-hidden="true"><circle cx="6" cy="6" r="6" fill="var(--pink)"/><path d="M4 3.2l1 1.6-.6.6c.4.8 1 1.4 1.8 1.8l.6-.6 1.6 1-.5 1.2C5.6 8.7 3.3 6.4 3 4z" fill="#fff"/></svg>
      0198 765 4321
    </p>
  </article>
</section>

</body>
</html>
```